Building Asset Management and Engineering Services for complex buildings

We provide asset management, project management, and engineering services for complex buildings.
Asset management services include, asset management strategies, plans, risk and conditioning assessments.
The engineering services include building services redesign, project management and commissioning services.

Target Market(s)

architects, government, electrical contractors

Industry/Entity Type

Asset Management

Contact Information for Business Card

KLT van Brommel QTSph, MKOrvia, DGLT, SMVK
Director
Other details such as address please refer to attached file

Font styles to use
Sans Serif

Requirements
Must have
• Fellow and Engineers logo on the back
• * Strategic Planning
• * Design
• * Documentation
• * Project Management
• * Commissioning
• * Assessment/Review
• Must have Engineers logo and wording on the back as well
Nice to have
• Good use of all the logo colours

```html
<!DOCTYPE html>
<html lang="en">
<head>
<meta charset="utf-8">
<title>RTQ Consultants – Business Card</title>
<link href="https://fonts.googleapis.com/css2?family=Libre+Baskerville&family=Open+Sans:wght@400;600&display=swap" rel="stylesheet">
<style>
  :root {
    --page: #e9e7e3;
    --card: #ffffff;
    --ink: #1d1d1d;
    --brand-blue: #4a97cf;
    --brand-red: #d6442b;
    --brand-green: #5cb63f;
    --band-dark: #141414;
    --band-text: #f2f2f2;
    --rule: #bdbdbd;
    --hatch-light: #f4f4f4;
    --hatch-mid: #d9d9d9;
  }
  * { box-sizing: border-box; margin: 0; padding: 0; }
  html, body { width: 1200px; height: 1000px; overflow: hidden; }
  body {
    background: var(--page);
    font-family: "Open Sans", Arial, sans-serif;
    color: var(--ink);
    display: flex;
    flex-direction: column;
    align-items: center;
    justify-content: center;
    gap: 60px;
  }
  .card {
    position: relative;
    width: 700px;
    height: 400px;
    background: var(--card);
    box-shadow: 0 6px 18px rgba(0,0,0,0.18);
    overflow: hidden;
  }

  /* Contact side */
  .brand-row {
    position: absolute;
    top: 34px; left: 0; right: 0;
    display: flex;
    justify-content: center;
    align-items: center;
    gap: 14px;
  }
  .brand-small {
    display: flex; align-items: center; gap: 8px;
    color: var(--brand-blue);
    font-weight: 600;
    font-size: 30px;
    letter-spacing: 1px;
    line-height: 1;
  }
  .brand-small .dot { width: 18px; height: 18px; border-radius: 50%; background: var(--brand-blue); }
  .badge { width: 26px; height: 26px; background: var(--brand-red); }
  .person {
    position: absolute; top: 100px; left: 0; right: 0; text-align: center;
  }
  .person-name {
    font-family: "Libre Baskerville", Georgia, serif;
    font-size: 26px;
  }
  .person-title { font-size: 14px; margin-top: 4px; }
  .contact {
    position: absolute; top: 185px; left: 90px; right: 90px;
    display: grid; grid-template-columns: 1fr 1px 1fr; column-gap: 34px;
    font-size: 16px; line-height: 1.45;
  }
  .contact .divider { background: var(--rule); height: 70px; }
  .contact .address { text-align: right; padding-top: 26px; }
  .contact .email { margin-top: 22px; }
  .hatch-band {
    position: absolute; left: 0; right: 0; bottom: 18px; height: 58px;
    background: linear-gradient(90deg, var(--hatch-light), var(--hatch-mid) 50%, var(--hatch-light));
  }

  /* Back side */
  .hatch-top {
    position: absolute; left: 0; right: 0; top: 0; height: 26px;
    background: linear-gradient(90deg, var(--hatch-light), var(--hatch-mid) 50%, var(--hatch-light));
  }
  .brand-large {
    position: absolute; top: 92px; left: 0; right: 0;
    display: flex; justify-content: center; align-items: center; gap: 22px;
    color: var(--brand-blue); font-weight: 600;
  }
  .brand-large .dot { width: 70px; height: 70px; border-radius: 50%; background: var(--brand-blue); }
  .brand-large .wordmark { line-height: 1; }
  .brand-large .wordmark-main { font-size: 88px; letter-spacing: 2px; }
  .brand-large .wordmark-sub { font-size: 15px; letter-spacing: 1.5px; margin-top: 6px; }
  .services-band {
    position: absolute; left: 0; right: 0; bottom: 0; height: 118px;
    background: var(--band-dark);
    color: var(--band-text);
    display: flex; flex-direction: column; justify-content: center; align-items: flex-end;
    padding-right: 36px;
    font-size: 17px; line-height: 1.5;
  }
</style>
</head>
<body>
  <section class="card card-contact" aria-label="Contact side">
    <div class="brand-row">
      <div class="brand-small"><span class="dot"></span>RTQ</div>
      <div class="badge" role="img" aria-label="Professional membership badge"></div>
    </div>
    <div class="person">
      <h1 class="person-name">KLT van Brommel</h1>
      <p class="person-title">QTSph, MKOrvia, DGLT, SMVK Director</p>
    </div>
    <div class="contact">
      <div class="address">
        PO Box 512K Ferndale North<br>
        Victoria Australia 3481
      </div>
      <div class="divider"></div>
      <div class="numbers">
        P: 0361552907<br>
        M: 0428306615
        <p class="email">E: klt.rtq@mailnest.com</p>
      </div>
    </div>
    <div class="hatch-band" role="img" aria-label="Fine diagonal line texture band"></div>
  </section>

  <section class="card card-brand" aria-label="Brand side">
    <div class="hatch-top" role="img" aria-label="Fine diagonal line texture band"></div>
    <div class="brand-large">
      <span class="dot"></span>
      <div class="wordmark">
        <div class="wordmark-main">RTQ</div>
        <div class="wordmark-sub">CONSULTANTS VIC PTY LTD</div>
      </div>
    </div>
    <div class="services-band">
      <p>Strategic Planning | Design | Documentation | Project Management</p>
      <p>Commissioning | Assessment/Review</p>
    </div>
  </section>
</body>
</html>
```